New concept for existing event brand

I have this current brand - www.velltrix-quarter.com I have attached an example of a credible event on 23rd December and then a more fun brunch event.

I require a new flyer for a new concept - Fernwick Frolics - (there is no logo yet) it is at a venue which has ball pits, table tennis, beer pong, arcades etc

I am looking for an artwork which portrays a fun event but also retains the cooler brand identify

One idea was having the images in polaroid frames

Fernwick Frolics

Saturday 18th February 2023

Venue to be announced • 3pm-9pm

2 giant ball pits
Beer pong
Ping Pong
Boxing machines
Dance Machine
Air Hockey
Pool
Giant board games
Giant Stackle 6
Photo Booth
Spin The Wheel
Table Football
Retro Arcade Games
Pinball

Food
Pizzas
Brimsy Bowls
Popcorn
Candy Floss

Cocktails
Alcoholic Chillo Kittens
Beer Towers
Spirits & Mixers

```html
<!DOCTYPE html>
<html lang="en">
<head>
<meta charset="utf-8">
<title>Fernwick Frolics – Flyer</title>
<link href="https://fonts.googleapis.com/css2?family=Montserrat:ital,wght@0,400;0,600;0,800;1,900&display=swap" rel="stylesheet">
<style>
  :root {
    --canvas: #ececec;
    --night: #14061f;
    --plum: #3a0f4f;
    --violet: #6a1f8a;
    --neon: #ff3fb4;
    --neon-soft: #ff8ad6;
    --white: #ffffff;
    --muted: #d9c8e6;
  }
  * { box-sizing: border-box; margin: 0; padding: 0; }
  html, body { width: 816px; height: 1200px; overflow: hidden; }
  body {
    background: var(--canvas);
    font-family: "Montserrat", Arial, sans-serif;
    color: var(--white);
    position: relative;
  }
  .page {
    position: absolute;
    top: 323px;
    width: 392px;
    height: 554px;
    background: var(--night);
    overflow: hidden;
    box-shadow: 0 6px 18px rgba(0,0,0,.25);
  }
  .page--front { left: 12px; }
  .page--back { left: 412px; }

  .crowd-photo {
    position: absolute; inset: 0;
    background:
      radial-gradient(ellipse at 50% 35%, rgba(230,120,255,.55), transparent 55%),
      radial-gradient(ellipse at 20% 60%, rgba(255,63,180,.35), transparent 50%),
      linear-gradient(180deg, #2a0b40 0%, #4d1570 45%, #1a0728 75%, #0e0418 100%);
  }
  .neon-frame { position: absolute; overflow: visible; }
  .neon-frame polygon {
    fill: none; stroke: var(--neon); stroke-width: 3;
    filter: drop-shadow(0 0 6px var(--neon));
  }

  .brand-name {
    position: absolute; left: 0; right: 0;
    text-align: center;
    font-weight: 800;
    text-transform: uppercase;
    color: var(--white);
    letter-spacing: .5px;
  }
  .page--front .brand-name { top: 64px; font-size: 27px; line-height: 1.05; }

  .event-title {
    position: absolute; left: 0; right: 0; top: 356px;
    text-align: center;
    font-weight: 900; font-style: italic;
    font-size: 40px; line-height: .95;
    text-transform: uppercase;
    text-shadow: 0 0 10px rgba(255,63,180,.6);
  }
  .event-date {
    position: absolute; left: 0; right: 0; top: 448px;
    text-align: center; color: var(--neon);
    font-weight: 800; font-size: 16px; text-transform: uppercase;
  }
  .event-date sup { font-size: 9px; }
  .event-venue {
    position: absolute; left: 0; right: 0; top: 470px;
    text-align: center; font-size: 7px; font-weight: 600;
    letter-spacing: 1px; text-transform: uppercase; color: var(--muted);
  }
  .event-time {
    position: absolute; left: 0; right: 0; top: 482px;
    text-align: center; font-weight: 900; font-style: italic;
    font-size: 24px;
  }
  .web-bar {
    position: absolute; left: 80px; right: 80px; bottom: 14px;
    height: 16px; border-radius: 8px;
    background: var(--neon);
    text-align: center; font-size: 8px; font-weight: 800;
    line-height: 16px; text-transform: uppercase; color: var(--white);
  }
  .page--back .web-bar { left: 200px; right: 16px; }

  /* back */
  .back-glow {
    position: absolute; inset: 0;
    background:
      radial-gradient(ellipse at 70% 80%, rgba(106,31,138,.6), transparent 60%),
      linear-gradient(180deg, #1d0830 0%, #14061f 100%);
  }
  .photo-tri { position: absolute; }
  .activities, .refreshments {
    position: absolute; top: 250px; list-style: none;
    font-size: 7.5px; font-weight: 600; line-height: 13px;
    text-transform: uppercase;
  }
  .activities { left: 24px; }
  .refreshments { left: 210px; }
  .activities li::before, .refreshments li::before {
    content: ""; display: inline-block; width: 4px; height: 4px;
    background: var(--neon); margin-right: 6px; vertical-align: middle;
  }
  .refreshments .group-head {
    color: var(--neon); font-weight: 800; font-size: 9px; margin-top: 6px;
  }
  .refreshments .group-head::before { display: none; }
  .page--back .brand-name {
    top: auto; bottom: 40px; left: 200px; right: 16px;
    font-size: 18px; line-height: 1.05;
  }
  .contact {
    position: absolute; left: 24px; bottom: 14px;
    display: flex; align-items: center; gap: 6px;
    font-size: 9px; font-weight: 800;
  }
  .contact small { display: block; font-size: 6px; font-weight: 600; color: var(--muted); }
</style>
</head>
<body>

<section class="page page--front">
  <div class="crowd-photo" role="img" aria-label="Party crowd with raised hands under purple stage lights"></div>
  <svg class="neon-frame" style="left:56px;top:26px" width="280" height="250" viewBox="0 0 280 250">
    <polygon points="140,8 272,242 8,242"/>
  </svg>
  <div class="brand-name">Velltrix<br>Quarter</div>
  <h1 class="event-title">Fernwick<br>Frolics</h1>
  <div class="event-date">Saturday 18<sup>th</sup> February 2023</div>
  <div class="event-venue">Venue to be announced</div>
  <div class="event-time">3PM-9PM</div>
  <div class="web-bar">www.velltrix-quarter.com</div>
</section>

<section class="page page--back">
  <div class="back-glow"></div>
  <svg class="photo-tri" style="left:20px;top:14px" width="360" height="230" viewBox="0 0 360 230">
    <defs>
      <linearGradient id="photoA" x1="0" y1="0" x2="1" y2="1">
        <stop offset="0" stop-color="#c44a9e"/><stop offset="1" stop-color="#3a0f4f"/>
      </linearGradient>
      <linearGradient id="photoB" x1="0" y1="0" x2="1" y2="1">
        <stop offset="0" stop-color="#5a7ad8"/><stop offset="1" stop-color="#7a1f6a"/>
      </linearGradient>
    </defs>
    <polygon points="10,10 180,10 95,160" fill="url(#photoA)" role="img" aria-label="Photo of guests enjoying drinks at a party"/>
    <polygon points="240,40 350,220 130,220" fill="url(#photoB)" role="img" aria-label="Photo of friends playing in a giant ball pit"/>
    <polygon points="10,10 180,10 95,160" fill="none" stroke="#ff3fb4" stroke-width="3" style="filter:drop-shadow(0 0 5px #ff3fb4)"/>
    <polygon points="240,40 350,220 130,220" fill="none" stroke="#ff3fb4" stroke-width="3" style="filter:drop-shadow(0 0 5px #ff3fb4)"/>
  </svg>
  <ul class="activities">
    <li>2 Giant Ball Pits</li>
    <li>Beer Pong</li>
    <li>Ping Pong</li>
    <li>Boxing Machines</li>
    <li>Dance Machine</li>
    <li>Air Hockey</li>
    <li>Pool</li>
    <li>Giant Board Games</li>
    <li>Giant Stackle 6</li>
    <li>Photo Booth</li>
    <li>Spin The Wheel</li>
    <li>Table Football</li>
    <li>Retro Arcade Games</li>
    <li>Pinball</li>
  </ul>
  <ul class="refreshments">
    <li class="group-head">Food</li>
    <li>Pizzas</li>
    <li>Brimsy Bowls</li>
    <li>Popcorn</li>
    <li>Candy Floss</li>
    <li class="group-head">Cocktails</li>
    <li>Alcoholic Chillo Kittens</li>
    <li>Beer Towers</li>
    <li>Spirits &amp; Mixers</li>
  </ul>
  <div class="contact">
    <svg width="16" height="16" viewBox="0 0 24 24" aria-hidden="true">
      <path fill="#ff3fb4" d="M6.6 10.8a15 15 0 0 0 6.6 6.6l2.2-2.2a1 1 0 0 1 1-.25 11.4 11.4 0 0 0 3.6.57 1 1 0 0 1 1 1V20a1 1 0 0 1-1 1A17 17 0 0 1 3 4a1 1 0 0 1 1-1h3.5a1 1 0 0 1 1 1c0 1.25.2 2.45.57 3.6a1 1 0 0 1-.25 1z"/>
    </svg>
    <span><small>Call us today</small>0 120 555 0147</span>
  </div>
  <div class="brand-name">Velltrix<br>Quarter</div>
  <div class="web-bar">www.velltrix-quarter.com</div>
</section>

</body>
</html>
```